Vell-Stackers web design

We need a homepage web design with final files to be provided in PSD for a company based in Brisbane called 'Vell-Stackers'. They provide innovative and reliable contract packaging solutions for local and national outsourcing buisnesses.

They have an existing website www.vell-stackers-example.com.au that is in dire need of an update to look more professional and sleek.

Target Market(s)

Engineers, Architects

Industry/Entity Type

Construction

Number of Pages Required

1 page

Requirements
Must have
• Main Navigation
• o Home
• o About Us
• o Spacers
• - Standard Cage Wheel Spacer
• - Heavy Duty Cage Wheel Spacer
• - Pile Cage Foot
• - PreCast Piles
• o Packaging
• o Injection Moulding
• o News
• o Contact Us
• - Client wants an updated more professional look and feel that aligns with their branding.
• - Client likes the use of displaying Products on every page eg www.gravelbrace-example.com that has an image of the product and its name obviously looking better than this.
• The following elements are to be included in the Homepage design concept:
• - Room for a Flash banner of rotating images
• - Horizontal navigation (can you show how drop down will appear as well)
• - Logo is attached
• - Phone number needs to appear prominently on every page 07 5918 4607
• - Use Arial font throughout concept incl logo
• - Intro text on page somewhere
• - Products need to be listed on page somewhere there are 7 products (image and name with click through)
• - 2 containers/icons to highlight areas on site Latest News and Contact Us
• - Images – have attached a few that can be used in concepts and also below are some pixquarry images that could be used in banner:
• http://www.pixquarry-example.com/stock-photo-4826153-several-paint-buckets.php
• http://www.pixquarry-example.com/stock-photo-3158207-cans-of-paint.php
• http://www.pixquarry-example.com/stock-photo-8047391-reinforcing-steel.php
• http://www.pixquarry-example.com/stock-photo-2693845-huge-bridge-pier.php
• http://www.pixquarry-example.com/stock-photo-9381427-highway-bridge.php
• http://www.pixquarry-example.com/stock-photo-1470638-bridge.php
• http://www.pixquarry-example.com/stock-photo-6205914-bridge-to-nowhere-yet.php

```html
<!DOCTYPE html>
<html lang="en">
<head>
<meta charset="utf-8">
<title>Vell-Stackers — Contract Packaging Brisbane</title>
<link href="https://fonts.googleapis.com/css2?family=Arimo:wght@400;700&display=swap" rel="stylesheet">
<style>
:root{
  --red:#b0080c;
  --red-bright:#d8121a;
  --black:#000;
  --ink:#fff;
  --panel:#3f3d3c;
  --panel-dark:#2e2c2b;
  --grey-top:#5d5a59;
  --grey-bottom:#c9c9c9;
  --line:#9a9a9a;
}
*{box-sizing:border-box;margin:0;padding:0}
html,body{width:867px;height:1200px;overflow:hidden;background:var(--red)}
body{font-family:"Arimo",Arial,sans-serif;color:var(--ink);position:relative}
.page{position:absolute;left:12px;top:0;width:843px;height:1200px;background:#000;overflow:hidden}
.abs{position:absolute}

/* header */
.header{left:0;top:0;width:843px;height:127px;
  background:radial-gradient(ellipse 420px 90px at 430px 40px,#d9d9d9 0%,#8a8a8a 35%,#1a1a1a 75%,#000 100%)}
.brand{left:70px;top:36px;display:flex;align-items:center;gap:10px}
.brand-dot{width:46px;height:46px;border-radius:50%;background:var(--red-bright)}
.brand-name{font-size:18px;font-weight:700;color:#e8e8e8}
.phone{left:574px;top:41px;width:217px;height:44px;border-radius:6px;
  background:linear-gradient(#e21a20,#9c0609);border:1px solid #ff6a6a;
  display:flex;align-items:center;justify-content:center;gap:6px;
  font-size:29px;font-weight:700;letter-spacing:-0.5px}

/* navigation */
.nav{left:0;top:127px;width:843px;height:31px;background:linear-gradient(#8c8c8c,#4a4a4a 45%,#1e1e1e)}
.nav-item{position:absolute;top:10px;font-size:10.5px;font-weight:700;color:#eee;white-space:nowrap}
.nav-sep{position:absolute;top:10px;width:1px;height:11px;background:#777}
.dropdown{left:274px;top:150px;width:145px}
.dropdown div{height:15px;margin-bottom:0.3px;background:#222;color:#eee;font-size:9.5px;text-align:center;line-height:15px;border-bottom:1px solid #777}
.dropdown .active{background:#d2240f}

/* hero */
.hero{left:0;top:158px;width:843px;height:217px;background:#fff}
.hero-photo{left:0;top:158px;width:300px;height:217px;background:linear-gradient(120deg,#f2f2f2,#cfcfcf 50%,#efefef)}
.flash{left:505px;top:187px;width:328px;height:161px;border-radius:8px;
  background:linear-gradient(90deg,#a8a8a8,#dedede);display:flex;align-items:center;justify-content:center;
  font-size:16px;color:#fff}

/* main */
.main{left:0;top:375px;width:843px;height:734px;background:linear-gradient(#5d5a59,#7a7878 40%,#c9c9c9)}
.welcome h1{font-size:14px;font-weight:700}
.welcome{left:25px;top:397px;width:480px}
.welcome p{font-size:10.5px;line-height:12px;margin-top:5px}
.btn{position:absolute;border-radius:12px;background:linear-gradient(#7a7a7a,#1a1a1a 55%,#3a3a3a);
  border:1px solid #aaa;color:#fff;font-weight:700;text-align:center;box-shadow:0 1px 2px rgba(0,0,0,.5)}
.products-title{left:25px;top:524px;font-size:14px;font-weight:700}
.products{left:74px;top:551px;width:373px;height:516px;border-radius:14px;background:linear-gradient(#3a3a3a,#5a5a5a)}
.product{position:absolute;left:35px;width:300px;height:62px}
.thumb{position:absolute;left:0;top:0;width:73px;height:62px;background:linear-gradient(135deg,#fff,#d5d5d5);border:2px solid #888}
.product h2{position:absolute;left:82px;top:12px;font-size:13.5px;font-weight:700;font-variant:small-caps;letter-spacing:.8px;white-space:nowrap}
.product .rule{position:absolute;left:80px;top:30px;width:225px;border-top:1px dotted #bbb}
.product .btn{left:209px;top:35px;width:92px;height:20px;font-size:13px;line-height:18px}

/* feature */
.feature{left:518px;top:394px;width:308px;height:280px;border-radius:12px;background:var(--panel)}
.feature-bar{position:absolute;left:0;top:16px;width:308px;height:26px;background:var(--panel-dark);
  font-size:15px;font-weight:700;font-variant:small-caps;letter-spacing:1px;text-align:center;line-height:26px}
.feature-img{left:78px;top:51px;width:151px;height:120px;border-radius:6px;background:linear-gradient(135deg,#fff,#dcdcdc)}
.feature p{position:absolute;left:10px;top:184px;width:288px;font-size:12px;line-height:14px;text-align:center}
.arrow{position:absolute;top:97px}

.cta{left:562px;display:flex;align-items:center;gap:8px}
.cta .icon{width:56px;height:56px;border-radius:50%;background:var(--red);border:2px solid #e03030;display:flex;align-items:center;justify-content:center}
.cta span{font-size:22px;font-weight:700;letter-spacing:1px}

/* footer */
.footer{left:0;top:1109px;width:843px;height:91px;background:#000}
.footer .login{position:absolute;right:17px;top:18px;font-size:11px;font-weight:700}
.footer .links{position:absolute;right:17px;top:38px;font-size:10.5px;font-weight:700}
.footer .links i{font-style:normal;color:#777;margin:0 4px}
.footer .copy{position:absolute;right:15px;top:54px;font-size:10.5px;font-weight:700}
</style>
</head>
<body>
<div class="page">
  <header class="abs header"></header>
  <div class="abs brand"><div class="brand-dot"></div><div class="brand-name">Vell-Stackers</div></div>
  <div class="abs phone">
    <svg width="16" height="24" viewBox="0 0 16 24"><rect x="1" y="1" width="14" height="22" rx="3" fill="none" stroke="#fff" stroke-width="2"/><rect x="4" y="4" width="8" height="8" fill="#fff"/></svg>
    07 5918 4607
  </div>

  <nav class="abs nav">
    <span class="nav-item" style="left:137px">HOME</span><span class="nav-sep" style="left:183px"></span>
    <span class="nav-item" style="left:198px">ABOUT US</span><span class="nav-sep" style="left:260px"></span>
    <span class="nav-item" style="left:276px">SPACERS</span><span class="nav-sep" style="left:335px"></span>
    <span class="nav-item" style="left:350px">PACKAGING</span><span class="nav-sep" style="left:430px"></span>
    <span class="nav-item" style="left:444px">INJECTION MOULDING</span><span class="nav-sep" style="left:570px"></span>
    <span class="nav-item" style="left:585px">NEWS</span><span class="nav-sep" style="left:627px"></span>
    <span class="nav-item" style="left:643px">CONTACT US</span>
  </nav>

  <section class="abs hero"></section>
  <div class="abs hero-photo" role="img" aria-label="Product photos: container, end cap, pipe plug, pile chair and hinged pile wheel"></div>
  <div class="abs flash">Flash Banner</div>

  <div class="abs dropdown">
    <div>Standard Cage Wheel Spacer</div>
    <div class="active">Heavy Duty Cage Wheel Spacer</div>
    <div>Pile Cage Foot</div>
    <div>PreCast Piles</div>
  </div>

  <main class="abs main"></main>
  <section class="abs welcome">
    <h1>WELCOME TO Vell-Stackers!</h1>
    <p>Vell-Stackers Brisbane, providing innovative and reliable contract packaging solutions for local and national outsourcing buisnesses.</p>
    <p style="margin-top:12px">Vell-Stackers (QLD) PTY LTD is a wholly Australian business with a firm foundation in client relations which we feel is of utmost import with an ever-expanding customer base. As such we endeavour to hold true to our founding company objectives and look towards the future with great confidence.</p>
  </section>
  <a class="btn" style="left:376px;top:498px;width:107px;height:22px;font-size:14px;line-height:20px">read more</a>

  <div class="abs products-title">Vell-Stackers' Products</div>
  <section class="abs products">
    <div class="product" style="top:16px"><div class="thumb" role="img" aria-label="Hinged pile wheel"></div><h2>Hinged Pile Wheel</h2><div class="rule"></div><a class="btn">read more</a></div>
    <div class="product" style="top:86px"><div class="thumb" role="img" aria-label="Precast pile chair"></div><h2>Precast Pile Chair</h2><div class="rule"></div><a class="btn">read more</a></div>
    <div class="product" style="top:156px"><div class="thumb" role="img" aria-label="Pipe plug"></div><h2>Pipe Plugs</h2><div class="rule"></div><a class="btn">read more</a></div>
    <div class="product" style="top:227px"><div class="thumb" role="img" aria-label="Container with lid"></div><h2>Containers &amp; Lids</h2><div class="rule"></div><a class="btn">read more</a></div>
    <div class="product" style="top:297px"><div class="thumb" role="img" aria-label="End cap"></div><h2>End Cap</h2><div class="rule"></div><a class="btn">read more</a></div>
    <div class="product" style="top:366px"><div class="thumb" role="img" aria-label="Light weight web wheel"></div><h2>Light Weight Web Wheel</h2><div class="rule"></div><a class="btn">read more</a></div>
    <div class="product" style="top:436px"><div class="thumb" role="img" aria-label="Heavy duty wheel spacer"></div><h2>Heavy Duty wheel Spacer</h2><div class="rule"></div><a class="btn">read more</a></div>
  </section>

  <aside class="abs feature">
    <div class="feature-bar">Hinged Pile Wheel for Cages</div>
    <svg class="arrow" style="left:52px" width="28" height="20" viewBox="0 0 28 20"><path d="M12 2 4 10l8 8M24 2l-8 8 8 8" fill="none" stroke="#ccc" stroke-width="4"/></svg>
    <div class="abs feature-img" role="img" aria-label="Hinged pile wheel product photo"></div>
    <svg class="arrow" style="left:228px" width="28" height="20" viewBox="0 0 28 20"><path d="M4 2l8 8-8 8M16 2l8 8-8 8" fill="none" stroke="#ccc" stroke-width="4"/></svg>
    <p>Vell-Stackers' Hinged Pile Wheels are innovativly designed for most types of heavy-duty applications. They are available in 150mm and 100mm wheel diameters for 75mm and 50mm cover respectively.</p>
    <a class="btn" style="left:112px;top:243px;width:106px;height:24px;font-size:15px;line-height:22px">more info</a>
  </aside>

  <div class="abs cta" style="top:695px">
    <div class="icon"><svg width="22" height="32" viewBox="0 0 22 32"><rect x="2" y="2" width="18" height="28" rx="4" fill="#fff"/><rect x="7" y="7" width="8" height="18" fill="var(--red)"/></svg></div>
    <span>CONTACT US</span>
  </div>
  <div class="abs cta" style="top:748px">
    <div class="icon"><svg width="24" height="32" viewBox="0 0 24 32"><path d="M2 2h14l6 6v22H2z" fill="#fff"/><path d="M5 12h14M5 16h14M5 20h14M5 24h14" stroke="var(--red)" stroke-width="1.5"/></svg></div>
    <span>LATEST NEWS</span>
  </div>

  <footer class="abs footer">
    <div class="login">LOGIN</div>
    <div class="links">HOME<i>|</i>ABOUT US<i>|</i>SPACERS<i>|</i>PACKAGING<i>|</i>INJECTION MOULDING<i>|</i>NEWS<i>|</i>CONTACT US</div>
    <div class="copy">© 2009 VELL-STACKERS.com.au | All Rights Reserved</div>
  </footer>
</div>
</body>
</html>
```